Harbor Mortgage Relief

Please help us give our website a remake or a FACELIFT. It is not very good but it says what we need it to say. But the design is terrible.
I would like our new design font and logo to be used as the theme.

I also want more photos on the site.

I also want consistency with the pages so they look clean.

We want the professionals to do this, let's see what you got!

Thank you!
Updates

Project Deadline Extended
Reason: I can understand you want to be paid. So I will commit to the fee but I want you to have time to make a KICK ASS website for me dudes! Thanks

HI!  Just wanted to say thanks for your time on these.  A lot are great.  However the firefighters have nothing to do with Foreclosure.  We are saving peoples homes from the bank taking them and selling them.   I LOVE the house photos and the families on the website.  That is the direction we like.  THanks.

THANK U ALL FOR THE WORK!   I like a few ending in the numbers: 147  733  693  536  620  478  727  508     I will go over them and choose one soon.  Thank you.   You will be paid shortly. 

Requirements
Must have
• Bright, Upbeat photos. Color scheme should be in order. We like icons on the bottom. not just text.

```html
<!DOCTYPE html>
<html lang="en">
<head>
<meta charset="utf-8">
<title>Harbor Mortgage Relief</title>
<link href="https://fonts.googleapis.com/css2?family=Arimo:wght@400;700&display=swap" rel="stylesheet">
<style>
:root{
  --red:#e63e31;
  --red-dark:#b8281f;
  --ink:#1a1a1a;
  --white:#ffffff;
  --black:#070707;
}
*{margin:0;padding:0;box-sizing:border-box}
html,body{width:1200px;height:1050px;overflow:hidden}
body{font-family:"Arimo",Arial,sans-serif;color:var(--ink);background:#fff;position:relative}
.site{position:relative;width:1200px;height:1050px}
.header{position:absolute;left:0;top:0;width:1200px;height:140px;background:linear-gradient(#ffffff,#e4e4e4)}
.brand{position:absolute;left:113px;top:22px;display:flex;align-items:center;gap:12px}
.brand-mark{width:78px;height:78px;border-radius:50%;background:var(--red)}
.brand-name{font-weight:700;font-size:22px;line-height:20px;color:var(--red);text-transform:uppercase;width:200px}
.nav{position:absolute;left:628px;top:0;width:465px;height:37px;background:var(--red);border-radius:0 0 14px 14px;display:flex;justify-content:space-around;align-items:center;padding:0 14px}
.nav a{color:var(--white);font-weight:700;font-size:12px;text-decoration:none}
.call{position:absolute;right:122px;top:62px;text-align:right}
.call-label{color:var(--red);font-weight:700;font-size:18px;display:flex;align-items:center;justify-content:flex-end;gap:2px}
.call-number{font-weight:700;font-size:20px;color:var(--black)}
.hero{position:absolute;left:0;top:110px;width:1200px;height:370px}
.hero svg{display:block}
.tagline{position:absolute;left:111px;top:274px;color:var(--white);font-weight:700;font-size:20px;line-height:24px;letter-spacing:.5px;word-spacing:3px}
.welcome{position:absolute;left:371px;top:497px;width:707px}
.welcome h1{font-size:21px;color:var(--red);font-weight:700;padding-left:2px;padding-bottom:2px;border-bottom:1px solid var(--red)}
.copy{font-size:12px;line-height:18px;color:var(--ink)}
.welcome .copy{margin-top:4px}
.story{position:absolute;left:376px;top:697px;width:704px}
.story p+p{margin-top:18px}
.photo-card{position:absolute;border:3px solid var(--red);border-radius:8px;overflow:hidden;box-shadow:0 14px 10px -8px rgba(0,0,0,.15)}
.photo-card.couple{left:127px;top:515px;width:217px;height:144px;background:linear-gradient(160deg,#f3f1ea,#c9b89a 55%,#7c7c6e)}
.photo-card.family{left:123px;top:706px;width:219px;height:144px;background:linear-gradient(160deg,#d6d8dc,#a77a64 50%,#3a3436)}
.photo-card::after{content:"";position:absolute;left:0;right:0;bottom:0;height:14px;background:var(--red);border-radius:50% 50% 0 0/100% 100% 0 0}
.footer{position:absolute;left:0;top:898px;width:1200px;height:127px;background:linear-gradient(90deg,var(--red) 0%,#d8382c 60%,var(--red-dark) 100%)}
.footer-note{position:absolute;left:121px;top:14px;width:247px;color:var(--white);font-size:12px;line-height:18px;text-align:justify}
.footer-address{position:absolute;right:134px;top:29px;color:var(--white);font-size:12px;line-height:18px;text-align:right}
.footer-address strong{font-weight:700}
.bottom-bar{position:absolute;left:0;top:1025px;width:1200px;height:25px;background:var(--black);color:var(--white);font-size:12px}
.bottom-nav{position:absolute;left:118px;top:6px;display:flex;gap:32px}
.bottom-nav a{color:var(--white);text-decoration:none}
.copyright{position:absolute;right:108px;top:5px}
</style>
</head>
<body>
<div class="site">
  <header class="header">
    <div class="brand">
      <span class="brand-mark"></span>
      <span class="brand-name">Harbor Mortgage Relief</span>
    </div>
    <nav class="nav">
      <a href="#">Home</a><a href="#">About Us</a><a href="#">Services</a><a href="#">Financing Options</a><a href="#">Contact Us</a>
    </nav>
    <div class="call">
      <div class="call-label">
        <svg width="14" height="20" viewBox="0 0 14 20"><path d="M4 1 L7 1 L7 6 L5 7 C5 11 6 13 8 15 L10 14 L12 18 L9 19 C4 18 1 12 2 4 Z" fill="var(--red)"/></svg>Call Us
      </div>
      <div class="call-number">888-555-0142</div>
    </div>
  </header>

  <section class="hero">
    <svg width="1200" height="370" viewBox="0 0 1200 370">
      <defs>
        <linearGradient id="heroFill" x1="0" y1="0" x2="1" y2="1">
          <stop offset="0" stop-color="#b9d6ee"/>
          <stop offset=".5" stop-color="#cfdbe4"/>
          <stop offset=".75" stop-color="#9a8a7c"/>
          <stop offset="1" stop-color="#3a3a36"/>
        </linearGradient>
        <linearGradient id="tagBand" x1="0" y1="0" x2="1" y2="0">
          <stop offset="0" stop-color="#000" stop-opacity=".92"/>
          <stop offset=".85" stop-color="#000" stop-opacity=".85"/>
          <stop offset="1" stop-color="#000" stop-opacity=".2"/>
        </linearGradient>
      </defs>
      <path d="M0 8 Q600 40 1200 22 L1200 362 Q900 340 600 338 Q300 338 0 358 Z" fill="url(#heroFill)" role="img" aria-label="Photo of a smiling family in front of a brick two-storey house under a clear sky"/>
      <path d="M70 8 Q600 40 1200 20 L1200 32 Q700 40 280 22 Z" fill="var(--red)"/>
      <path d="M0 345 Q500 325 1200 352 L1200 370 L0 370 Z" fill="#fff"/>
      <path d="M0 340 Q450 322 860 338 Q600 332 0 358 Z" fill="var(--red)"/>
      <rect x="0" y="262" width="582" height="76" fill="url(#tagBand)"/>
    </svg>
    <div class="tagline">Offering&nbsp; solid alternatives<br>to&nbsp; losing&nbsp; your&nbsp; home&nbsp; in a Trustee&nbsp; Sale</div>
  </section>

  <div class="photo-card couple" role="img" aria-label="Photo of a couple embracing outside their house"></div>
  <div class="photo-card family" role="img" aria-label="Photo of a smiling family of five"></div>

  <section class="welcome">
    <h1>Welcome to Harbor Mortgage Relief</h1>
    <p class="copy">HARBOR MORTGAGE RELIEF specializes in assisting homeowners who are in FORECLOSURE, by offering solid alternatives to losing your home in a Trustee Sale.&nbsp; Having your home foreclosed on can damage your credit for up to 7 years.&nbsp; Most foreclosures end with the home owner being evicted from their home, leaving them with no money, no place to live and without ample time to safely remove their possessions from their home.&nbsp; There is no need to have this happen to you.&nbsp; No matter what part of foreclosure process you are in, WE CAN HELP!<br>If you have received a Notice of Default (NOD) or Notice of Trustee Sale (NTS), you have options.&nbsp; Contact us today to speak to one of our licensed specialist, and let us help you put this situation behind you.</p>
  </section>

  <section class="story copy">
    <p>We speak to hundreds of homeowners every day, we understand how frustrating this can be.&nbsp; Don't live in fear of what is to come. You have other options, please call or email us today and we will immediately put our specialist to work finding you a solution.</p>
    <p>Don't try to handle this frustrating situation by yourself.&nbsp; HARBOR MORTGAGE RELIEF is a team of knowledgeable real estate professionals, we can offer you a better solution during this tough time.</p>
    <p>HARBOR MORTGAGE RELIEF&nbsp; has been assisting families in foreclosure for years.&nbsp; Our skill and integrity has earned us a reputation for fast, professional, courteous and thorough solutions.&nbsp; With over 50 years of real estate knowledge and experience HARBOR MORTGAGE RELIEF is ready to assist you.</p>
  </section>

  <footer class="footer">
    <p class="footer-note">Si el banco esta a punto de subastar su casa! No se den por vencidos.&nbsp; Estamos aqui para proveerles opciones.<br>Hablenos al numero 888-555-0142 para una consulta gratuita.&nbsp;&nbsp;&nbsp; Hablamos Espanol.</p>
    <address class="footer-address" style="font-style:normal">
      <strong>HARBOR MORTGAGE RELIEF</strong><br>
      118 Harbor Lane, Suite 200<br>
      Bayview, CA 90210<br>
      Call us : 888-555-0142
    </address>
  </footer>
  <div class="bottom-bar">
    <nav class="bottom-nav"><a href="#">Home</a><a href="#">About Us</a><a href="#">Services</a><a href="#">Financing Options</a><a href="#">Contact Us</a></nav>
    <div class="copyright">Content copyright 2012. HARBORMORTGAGERELIEF.COM. All rights reserved.</div>
  </div>
</div>
</body>
</html>
```